Website Design for a different kind of Business Consulting organisation needed!

We need a website design that reflects who we are, the simplicity of our consulting business and with a focus on our priority - to help our clients deliver, or execute - the "e" in Vantor-o.

Our key high level requirements are:
1) Simple and intuitive look and feel
2) Integration with all key social media platforms, chirpline, friendwall, workmesh, blogvine.

10 pages, tops.
- Main page - Welcome
- About Us/ Who are Vantor-o?
- 5 services pages - Project Management, Business Process Management, Change Management, Business Analysis and Finance Systems
- Contact Us

Something like:
http://www.hlmworks.example/

Vantor-o is a registered trademark and all Logos and other branded material are attached for reference.

So, what’s our gig: A few snippets from previous work...

We are a different kind of business consulting group. We partner with our clients to help them deliver change. We don't just provide them with the theory. We also provide them with the leadership and capability to execute the change.

We aren’t a one stop shop, and we don’t offer cookie cutter solutions. We’re a boutique consulting firm covering Project Management, Business Process Management, Change Management and Business Analytics.

Vantor-o is a professional services organisation that partners with their clients to lead the execution of strategic process and system improvement initiatives. Vantor-o combines hands on delivery with coaching in best practice methodologies and approaches to build their clients capabilities to ensure their ongoing success in project implementations.

UPDATES:

Thanks to everyone who has submitted designs so far. The standard of designs coming through is quite high, with lots of professional designs that nail the design brief. Eliminating them is proving to be quite challenging.

A few updates to the job brief:
- Please make sure the design fits on one page. We would like all of our information to be on the first page that people see without them having to scroll down
- Please ensure you include the FIVE services we offer in the design
- Please use corporate images/snapvault photos in your designs which are relevant to our business
- Please add a section for a live chirpline feed from our chirpline account and a link to circlenet+
- Please add a section for news/updates

Also, if you are able to build a site once a design is selected, please let us know.

Thanks,

Marisol.

Target Market(s)

Our target customers are large enterprises in Australia that are growing rapidly and have recently (last 24 months) undertaken or are currently undergoing software implementations and business process improvement programs. These businesses have a turnover of $100m or above and are working hard to differentiate themselves from their competitors but are not seeing the return on investment promised by software vendors and process improvement initiatives.

Industry/Entity Type

Leadership

Requirements
Must have
• Collaboration / Training / Workshop / Consulting images all of a professional nature.
Simple, non-cluttered look with plenty of white space.

```html
<!DOCTYPE html>
<html lang="en">
<head>
<meta charset="utf-8">
<title>Vantor-o — Contact</title>
<link rel="stylesheet" href="https://fonts.googleapis.com/css2?family=Open+Sans:wght@400;600;700&display=swap">
<style>
  :root {
    --brand: #0a51a0;
    --brand-dark: #074185;
    --text: #333333;
    --heading-grey: #444444;
    --nav-grey: #8c8c8c;
    --icon-grey: #7a7a7a;
    --field-border: #c9c9c9;
    --placeholder: #b5b5b5;
    --white: #ffffff;
    --map-base: #ece7dc;
    --map-accent: #cfe0ee;
  }
  * { box-sizing: border-box; margin: 0; padding: 0; }
  html, body { width: 1067px; height: 1200px; overflow: hidden; background: var(--white); }
  body { font-family: "Open Sans", Arial, sans-serif; color: var(--text); position: relative; }
  .top-band { position: absolute; left: 0; top: 0; width: 1067px; height: 6px; background: var(--brand); }

  .brand-name { position: absolute; left: 107px; top: 28px; font-size: 42px; font-weight: 600; color: var(--brand); letter-spacing: 0.5px; line-height: 50px; }

  .social-top { position: absolute; left: 820px; top: 16px; display: flex; gap: 9px; }
  .social-top span { width: 28px; height: 28px; border-radius: 50%; background: var(--icon-grey); display: block; }
  .social-top span.active { background: var(--brand); }

  .main-nav { position: absolute; left: 463px; top: 63px; display: flex; font-size: 15px; color: var(--nav-grey); }
  .main-nav a { color: inherit; text-decoration: none; line-height: 21px; margin-right: 47px; }
  .main-nav a.current { position: absolute; left: 413px; top: 0; background: var(--brand); color: var(--white); padding: 0 9px; margin: 0; }

  .map { position: absolute; left: 106px; top: 101px; width: 852px; height: 290px; background: linear-gradient(135deg, var(--map-base) 0%, #efe3c8 45%, var(--map-accent) 100%); }

  .page-title { position: absolute; left: 106px; top: 414px; font-size: 27px; font-weight: 700; color: var(--brand); }
  .intro { position: absolute; left: 106px; top: 449px; width: 860px; font-size: 14.5px; line-height: 22px; color: var(--text); }

  .section-title { position: absolute; font-size: 19px; font-weight: 600; color: var(--heading-grey); }
  .form-title { left: 105px; top: 538px; }
  .details-title { left: 667px; top: 531px; }

  .field-label { position: absolute; left: 106px; font-size: 14.5px; color: var(--text); }
  .field { position: absolute; left: 106px; width: 448px; height: 29px; border: 1px solid var(--field-border); font-size: 14.5px; color: var(--placeholder); padding: 3px 12px; line-height: 21px; }
  .field.focused { border: 2px solid var(--brand); padding: 2px 11px; }
  .field.message { height: 124px; }

  .captcha-label { position: absolute; top: 924px; font-size: 14.5px; }
  .captcha-input { position: absolute; left: 106px; top: 946px; width: 121px; height: 29px; border: 1px solid var(--field-border); font-size: 12.5px; color: var(--placeholder); padding: 5px 7px; }
  .captcha-code { position: absolute; left: 241px; top: 946px; width: 108px; height: 29px; border: 1px solid var(--field-border); background: linear-gradient(90deg, #f4f4f4, #dcdcdc, #f4f4f4); }
  .refresh { position: absolute; left: 281px; top: 926px; width: 16px; height: 16px; border: 1px solid #777; }

  .submit { position: absolute; left: 442px; top: 940px; width: 106px; height: 34px; background: var(--brand); color: var(--white); font-size: 14.5px; text-align: center; line-height: 34px; }

  .contact-lines { position: absolute; left: 667px; top: 581px; font-size: 14.5px; line-height: 23px; }
  .contact-row { position: absolute; left: 667px; display: flex; align-items: center; font-size: 14.5px; }
  .contact-row svg { width: 19px; height: 19px; margin-right: 9px; }

  .footer { position: absolute; left: 0; top: 1081px; width: 1067px; height: 119px; background: var(--brand); color: var(--white); font-size: 11px; line-height: 17px; }
  .footer h4 { font-size: 12.5px; font-weight: 700; line-height: 18px; margin-bottom: 1px; }
  .footer .col { position: absolute; top: 17px; }
  .footer .social-foot { display: flex; gap: 9px; margin-top: 6px; }
  .footer .social-foot span { width: 28px; height: 28px; border-radius: 50%; background: var(--white); display: block; }
  .footer .links { display: flex; gap: 26px; }
  .footer-brand { position: absolute; left: 769px; top: 14px; font-size: 36px; font-weight: 600; line-height: 40px; }
  .footer-copy { position: absolute; left: 770px; top: 66px; }
</style>
</head>
<body>
  <div class="top-band"></div>

  <div class="brand-name">Vantor-o</div>

  <div class="social-top" aria-label="Social links">
    <span aria-label="circlenet+"></span>
    <span class="active" aria-label="friendwall"></span>
    <span aria-label="workmesh"></span>
    <span aria-label="chirpline"></span>
  </div>

  <nav class="main-nav">
    <a href="#">HOME</a>
    <a href="#">ABOUT</a>
    <a href="#">SERVICES</a>
    <a href="#">PARTNERS</a>
    <a href="#" class="current">CONTACT</a>
  </nav>

  <div class="map" role="img" aria-label="Street map of the city centre showing the office location beside the river"></div>

  <h1 class="page-title">Contact Us</h1>
  <p class="intro">Sed ut perspiciatis unde omnis iste natus error sit voluptatem accusantium doloremque laudantium, totam rem aperiam, eaque ipsa quae ab illo inventore veritatis et quasi architecto beatae vitae dicta sunt explicabo.</p>

  <h2 class="section-title form-title">Contact Form</h2>
  <div class="field-label" style="top:570px">Name:</div>
  <div class="field" style="top:592px">Enter you name</div>
  <div class="field-label" style="top:634px">Email Address:</div>
  <div class="field focused" style="top:656px">Enter your email</div>
  <div class="field-label" style="top:700px">Subject:</div>
  <div class="field" style="top:723px">Enter subject</div>
  <div class="field-label" style="top:766px">Message:</div>
  <div class="field message" style="top:788px">Enter Message</div>

  <div class="captcha-label" style="left:106px">Type code shown</div>
  <div class="captcha-label" style="left:241px">Code:</div>
  <div class="refresh"></div>
  <div class="captcha-input">Type Code here</div>
  <div class="captcha-code" role="img" aria-label="Distorted verification code"></div>
  <div class="submit">Submit</div>

  <h2 class="section-title details-title">Contact Details</h2>
  <div class="contact-lines">Level 10, 42 Harbour Lane, Eastbridge<br>Australia, 3999</div>

  <div class="contact-row" style="top:634px">
    <svg viewBox="0 0 20 20"><circle cx="10" cy="10" r="10" fill="#0a51a0"/><path d="M6 8c0-2 8-2 8 0v1h-2V8H8v1H6z M7 10h6l1 4H6z" fill="#fff"/></svg>
    +61 3 555 014 202
  </div>
  <div class="contact-row" style="top:661px">
    <svg viewBox="0 0 20 20"><circle cx="10" cy="10" r="10" fill="#0a51a0"/><rect x="7" y="5" width="6" height="4" fill="#fff"/><rect x="5" y="9" width="10" height="5" fill="#fff"/><rect x="7" y="12" width="6" height="3" fill="#0a51a0"/></svg>
    +61 3 5550 1388
  </div>
  <div class="contact-row" style="top:690px">
    <svg viewBox="0 0 20 20"><circle cx="10" cy="10" r="10" fill="#0a51a0"/></svg>
    @vantor-o
  </div>
  <div class="contact-row" style="top:717px">
    <svg viewBox="0 0 20 20"><circle cx="10" cy="10" r="10" fill="#0a51a0"/><rect x="5" y="6.5" width="10" height="7" fill="#fff"/><path d="M5 6.5l5 4 5-4" fill="none" stroke="#0a51a0" stroke-width="1.2"/></svg>
    info@vantor-o.example
  </div>

  <footer class="footer">
    <div class="col" style="left:107px">
      <h4>CONNECT WITH US</h4>
      <div>on social media network</div>
      <div class="social-foot">
        <span aria-label="circlenet+"></span>
        <span aria-label="friendwall"></span>
        <span aria-label="workmesh"></span>
        <span aria-label="chirpline"></span>
      </div>
    </div>
    <div class="col" style="left:293px">
      <h4>PAGES</h4>
      <div class="links">
        <div>Home<br>About<br>Services</div>
        <div>Term &amp; Conditions<br>FAQ<br>Partners</div>
      </div>
    </div>
    <div class="col" style="left:505px">
      <h4>CONTACT DETAILS</h4>
      <div>p: +61 3 555 014 202&nbsp; f: +61 3 5550 1388<br>Level 10, 42 Harbour Lane, Eastbridge,<br>Australia, 3999</div>
    </div>
    <div class="footer-brand">Vantor-o</div>
    <div class="footer-copy">Copyright © 2014 All Rights Reserved</div>
  </footer>
</body>
</html>
```